LOS PINOS DE ARENA - EXCLUSIVE AND LUXURY REAL ESTATE PROJECT

Se trata del diseño de un mono poste grande (4 m x 2 m) o (8m x 3m) anunciando la construcción de 30 villas de lujo en un terreno en primera línea de playa en el sur de España (Cádiz).

La idea es crear expectación y transmitir lujo y exclusividad.

Target Market(s)

Clientes de alto poder adquisitivo que quieran adquirir su segunda vivienda en un entorno privilegiado a escasos pasos de una de las playas más bonitas de Cádiz.

Industry/Entity Type

REAL ESTATE

Colors

Designer to choose colors to be used in the design.

Requirements
Must have
• LOS PINOS DE ARENA as the name of the development
Nice to have
• Crear expectación con ideas del tipo: “Coming soon” o “No te lo puedes perder”

```html
<!DOCTYPE html>
<html lang="es">
<head>
<meta charset="utf-8">
<title>Los Pinos De Arena – Coming Soon</title>
<link rel="stylesheet" href="https://fonts.googleapis.com/css2?family=Roboto+Slab:wght@400&family=Cormorant+Garamond:wght@500&display=swap">
<style>
  :root {
    --page-bg: #e4e4e4;
    --board-black: #141414;
    --text-white: #ffffff;
    --gold-deep: #f3b81e;
    --gold-light: #fdf3b8;
    --gold-mid: #c9962e;
    --gold-pale: #f6eab0;
  }
  html, body {
    margin: 0;
    width: 1200px;
    height: 1000px;
    overflow: hidden;
    background: var(--page-bg);
  }
  .canvas {
    position: relative;
    width: 1200px;
    height: 1000px;
  }
  .billboard {
    position: absolute;
    left: 150px;
    top: 278px;
    width: 898px;
    height: 449px;
    background: var(--board-black);
  }
  .billboard-frame {
    position: absolute;
    left: 0;
    top: 0;
  }
  .tagline {
    position: absolute;
    left: 0;
    width: 100%;
    text-align: center;
    font-family: "Roboto Slab", Georgia, serif;
    font-weight: 400;
    font-size: 31px;
    color: var(--text-white);
    line-height: 1;
    margin: 0;
  }
  .tagline--top { top: 117px; }
  .tagline--bottom { top: 303px; }
  .headline {
    position: absolute;
    left: 0;
    width: 100%;
    top: 154px;
    text-align: center;
    margin: 0;
    font-family: "Cormorant Garamond", Garamond, serif;
    font-weight: 500;
    font-size: 108px;
    line-height: 1;
    letter-spacing: 1px;
    background: linear-gradient(90deg, var(--gold-deep) 0%, var(--gold-light) 30%, var(--gold-mid) 62%, var(--gold-pale) 100%);
    -webkit-background-clip: text;
    background-clip: text;
    color: transparent;
  }
</style>
</head>
<body>
<div class="canvas">
  <section class="billboard">
    <svg class="billboard-frame" width="898" height="449" viewBox="0 0 898 449" aria-hidden="true">
      <defs>
        <linearGradient id="gold-line" x1="0" y1="0" x2="1" y2="0">
          <stop offset="0" stop-color="#f3b81e"/>
          <stop offset="0.3" stop-color="#fdf3b8"/>
          <stop offset="0.62" stop-color="#c9962e"/>
          <stop offset="1" stop-color="#f6eab0"/>
        </linearGradient>
      </defs>
      <g fill="none" stroke="url(#gold-line)" stroke-width="3">
        <!-- upper bracket -->
        <polyline points="99,150 99,104 800,104 800,150"/>
        <!-- lower bracket -->
        <polyline points="99,299 99,346 800,346 800,299"/>
        <!-- central band -->
        <polygon points="90,160 815,160 842,224 815,289 90,289 57,224"/>
        <!-- inner uprights -->
        <line x1="99" y1="169" x2="99" y2="278"/>
        <line x1="800" y1="169" x2="800" y2="278"/>
      </g>
    </svg>
    <p class="tagline tagline--top">30 Villas De Lujo</p>
    <h1 class="headline">Coming Soon</h1>
    <p class="tagline tagline--bottom">Los Pinos De Arena</p>
  </section>
</div>
</body>
</html>
```